Post storm repair flyer

looking for an eye catching 6x9 postcard to send out to single family home owners advertising a "Post Storm Repair Special" explaining that after the recent hurricanes its very important to have your roof checked and any repairs fixed right away before they become a bigger more costly problem and that even though your home wasn't directly hit by the storm the high wind gust could've cause unseen damage.
offer $200 off any repair *some rules may apply
Lark Roofing
888.417.LARK
www.LarkRoofing.example

Roofing

```html
<!DOCTYPE html>
<html lang="en">
<head>
<meta charset="utf-8">
<title>Lark Roofing – Post Storm Repair Postcard</title>
<link rel="stylesheet" href="https://fonts.googleapis.com/css2?family=Lato:wght@400;700&family=Saira:wght@500;600&display=swap">
<style>
  :root {
    --backdrop: #8a94a2;
    --photo-dark: #262628;
    --photo-mid: #48484b;
    --ink-light: #ffffff;
    --ink-soft: #e2e2e4;
    --ink-dark: #111111;
    --band: #ffffff;
    --rule: #222222;
  }
  * { margin: 0; padding: 0; box-sizing: border-box; }
  html, body {
    width: 1200px;
    height: 1200px;
    overflow: hidden;
    background: var(--backdrop);
  }
  .postcard {
    position: absolute;
    left: 250px;
    top: 75px;
    width: 700px;
    height: 1050px;
    background: var(--band);
    box-shadow: 0 6px 24px rgba(0,0,0,0.25);
    overflow: hidden;
  }
  .roof-photo {
    position: absolute;
    left: 0; top: 0;
    width: 700px;
    height: 844px;
    background: linear-gradient(160deg, var(--photo-mid) 0%, var(--photo-dark) 45%, var(--photo-mid) 100%);
  }
  .special {
    position: absolute;
    left: 0; right: 0;
    top: 92px;
    text-align: center;
    font-family: "Saira", sans-serif;
    font-weight: 600;
    font-size: 40px;
    line-height: 1;
    letter-spacing: 2px;
    text-transform: uppercase;
    color: var(--ink-light);
  }
  .storm-message {
    position: absolute;
    left: 90px;
    width: 520px;
    top: 160px;
    text-align: center;
    font-family: "Lato", sans-serif;
    font-weight: 400;
    font-size: 21px;
    line-height: 1.5;
    color: var(--ink-soft);
  }
  .brand-name {
    position: absolute;
    left: 0; right: 0;
    top: 322px;
    text-align: center;
    font-family: "Lato", sans-serif;
    font-weight: 400;
    font-size: 34px;
    letter-spacing: 0.5px;
    color: var(--ink-light);
  }
  .headline {
    position: absolute;
    left: 0; right: 0;
    top: 520px;
    text-align: center;
    font-family: "Saira", sans-serif;
    font-weight: 600;
    font-size: 76px;
    line-height: 1;
    font-variant: small-caps;
    letter-spacing: 3px;
    color: var(--ink-light);
  }
  .offer {
    position: absolute;
    left: 0; right: 0;
    top: 690px;
    text-align: center;
    font-family: "Saira", sans-serif;
    font-weight: 500;
    color: var(--ink-light);
    line-height: 1;
    letter-spacing: 1.5px;
  }
  .offer-line { font-size: 23px; text-transform: uppercase; }
  .offer-amount { font-size: 40px; font-weight: 600; }
  .offer-rules {
    display: block;
    margin-top: 10px;
    font-size: 22px;
    text-transform: uppercase;
  }
  .contact {
    position: absolute;
    left: 0; right: 0;
    top: 893px;
    text-align: center;
    font-family: "Saira", sans-serif;
    font-weight: 600;
    color: var(--ink-dark);
    line-height: 1;
  }
  .contact-phone { font-size: 28px; letter-spacing: 1px; }
  .contact-web {
    margin-top: 12px;
    font-size: 24px;
    letter-spacing: 4px;
    font-variant: small-caps;
  }
  .footer-rule {
    position: absolute;
    left: 106px;
    top: 997px;
    width: 488px;
    height: 18px;
    background: var(--rule);
  }
</style>
</head>
<body>
  <main class="postcard">
    <div class="roof-photo" role="img" aria-label="Close-up photograph of dark asphalt roof shingles on a pitched roof"></div>
    <h2 class="special">Post Storm Repair Special</h2>
    <p class="storm-message">Even if your home wasn't directly hit, high wind gusts from the recent hurricanes can cause unseen roof damage. Get your roof checked and repaired now, before it becomes a bigger, more costly problem.</p>
    <div class="brand-name">LARKROOFING.EXAMPLE</div>
    <h1 class="headline">Lark Roofing</h1>
    <p class="offer">
      <span class="offer-line">offer <span class="offer-amount">$200 off</span> any repair</span>
      <span class="offer-rules">*some rules may apply</span>
    </p>
    <div class="contact">
      <p class="contact-phone">888.417.LARK</p>
      <p class="contact-web">www.LarkRoofing.example</p>
    </div>
    <div class="footer-rule"></div>
  </main>
</body>
</html>
```